IT services web page design

Hello!

We need new design for our web site, obviously :)

Our company is service oriented and we are maintaining, configuring and fixing problems for IT + selling other internet related services.

Our speciality are in area of internet services (web, dns, email, databases, backup...) and internet servers technology.

We also provide service and sales of Zentor Apps and Halvorix Quorvo365 for which we are certified by Zentor and Halvorix.

Other services that we provide (not so in focus) are: VPS hosting, remote backup, web hosting, vexalink fixing...

People mostly call us when they have a problems and this is core idea that new web site has to communicate - We can fix your server / web / email problems, save your money and as* :)

Our team have 15+ years experience with all range of internet technology + bunch of certificates from Halvorix and Tandix [we need to show people we have certificates].
Our qualities: experience, knowledge, delivery on time

In start we will not have blog section, but we need it in future. We also need place for plonkit feeds on web site.

Depth of the site should be max. level 2.

This site will go out in two languages so we need switch button on page from pone language to another.

Target Market(s)

small and mid size business that use internet services for daily operations and main business

Industry/Entity Type

Internet

Requirements
Must have
• * design should be in the way that responsive web could be made

Nice to have
• Long format will be OK for us. Like today pages that list all services and benefits on one loooong web page...

Logo is in attachment. It will be nice to have it on web site but if you find it not appropriate you can change it or put another one.

```html
<!DOCTYPE html>
<html lang="en">
<head>
<meta charset="utf-8">
<title>Kelvar grupa – IT Solutions</title>
<link rel="stylesheet" href="https://fonts.googleapis.com/css2?family=Raleway:wght@300;400;500;600&family=Roboto:wght@400;500;700;900&display=swap">
<style>
:root{
  --ink:#111;
  --panel:#1a1a1a;
  --sky-top:#d7eef8;
  --sky-mid:#9fd2ee;
  --stripe:#4fb0e6;
  --cyan:#45b6e8;
  --green:#4b9a45;
  --teal:#2fbfc4;
  --muted:#6a6a6a;
  --line:#c9c9c9;
  --white:#fff;
}
*{margin:0;padding:0;box-sizing:border-box}
html,body{width:1200px;height:1091px;overflow:hidden;background:var(--white)}
body{position:relative;font-family:"Raleway",sans-serif;color:#333}
.abs{position:absolute}
.sky{left:0;top:0;width:1200px;height:367px;background:linear-gradient(180deg,var(--sky-top) 0%,#c6e6f5 40%,var(--sky-mid) 100%)}
.topbar{left:0;top:0;width:1200px;height:5px;background:var(--ink)}
.stripe{left:0;top:370px;width:1200px;height:16px;background:var(--stripe)}
.lang{left:847px;top:5px;width:183px;height:23px;background:var(--ink);border-radius:0 0 6px 6px;color:var(--white);font:400 11px "Roboto",sans-serif;display:flex;align-items:center;padding-left:14px;gap:7px}
.lang .flag{width:16px;height:11px;background:#2a4a9a;border:1px solid #ccc}
.lang .caret{width:0;height:0;border-left:5px solid transparent;border-right:5px solid transparent;border-top:6px solid #888}
.logo{left:171px;top:58px;display:flex;align-items:center;gap:10px}
.logo-name{font:700 29px "Roboto",sans-serif;color:var(--ink);letter-spacing:.5px}
.logo-mark{width:72px;height:72px;border-radius:50%;background:#1d2a36}
.nav{left:453px;top:73px;display:flex;font:400 13px "Roboto",sans-serif;color:var(--ink)}
.nav a{color:inherit;text-decoration:none;padding:0 21px;border-left:1px dashed #666;line-height:17px}
.nav a:first-child{border-left:0;padding-left:0}
.nav a:last-child{padding-right:0}
.hero{left:171px;top:134px;width:858px;height:325px;background:linear-gradient(90deg,#3b4046 0%,#8c9299 40%,#6c7178 65%,#2a2d31 100%)}
.hero-text{left:236px;top:239px;color:var(--white);font-family:"Roboto",sans-serif;text-align:right}
.hero-text .small{font:900 16px "Roboto",sans-serif;text-align:left}
.hero-text .big{font:900 35px/1 "Roboto",sans-serif;margin-top:1px}
.hero-text .sub{font:900 16px "Roboto",sans-serif;margin-top:1px}
.service{top:471px;width:202px;height:116px;background:var(--panel);color:var(--white);border-bottom:4px solid #555;box-shadow:0 8px 8px -6px rgba(0,0,0,.25)}
.service h3{position:absolute;top:20px;font:500 17px "Roboto",sans-serif}
.service p{position:absolute;top:47px;font:400 10.5px/12px "Roboto",sans-serif;width:118px}
.service svg{position:absolute;left:12px;top:44px}
.service .notch{position:absolute;right:-8px;top:50px;width:0;height:0;border-top:10px solid transparent;border-bottom:10px solid transparent;border-left:8px solid var(--white)}
.welcome{left:181px;top:632px;font:400 33px "Raleway",sans-serif;color:var(--cyan)}
.vdivider{left:351px;top:639px;height:77px;border-left:1px dashed #999}
.intro{left:379px;top:638px;width:645px}
.intro h2{font:400 17px "Raleway",sans-serif;color:var(--green);margin-bottom:10px}
.intro p{font:400 11.8px/17px "Raleway",sans-serif;color:#333;letter-spacing:-.1px}
.intro a{color:var(--green);font-weight:500;text-decoration:none;margin-left:4px}
.hrule{left:170px;width:860px;border-top:1px dotted #aaa}
.section-title{font:500 18px "Raleway",sans-serif;color:#555}
.news-icon{left:181px;top:784px}
.news-item{top:827px;width:260px}
.date{position:absolute;left:0;top:0;width:33px;height:32px;background:var(--green);color:var(--white);text-align:center;font:700 14px/1 "Roboto",sans-serif;padding-top:3px}
.date span{display:block;font:400 9px "Roboto",sans-serif;margin-top:2px}
.news-item h4{position:absolute;left:46px;top:0;font:400 13px "Raleway",sans-serif;color:#333;white-space:nowrap}
.news-item p{position:absolute;left:46px;top:16px;font:400 10px "Roboto",sans-serif;color:#555;white-space:nowrap}
.btn{position:absolute;left:46px;top:45px;background:var(--ink);color:var(--white);font:400 10px "Roboto",sans-serif;padding:5px 7px;border-radius:2px;box-shadow:0 0 0 1px #888}
.tw-divider{left:743px;top:802px;height:80px;border-left:1px dashed #bbb}
.tweet-dot{left:761px;top:825px;width:26px;height:26px;border-radius:50%;background:var(--teal)}
.tweet{left:798px;top:825px;width:217px;height:36px;background:var(--teal);color:#123;font:400 11.5px/13px "Raleway",sans-serif;padding:4px 14px}
.tweet::before{content:"";position:absolute;left:-7px;top:5px;border-top:6px solid transparent;border-bottom:6px solid transparent;border-right:7px solid var(--teal)}
.follow{left:798px;top:872px;font:400 10px "Roboto",sans-serif;color:#556;border:1px solid #ccd;background:#f4f6fa;padding:4px 5px;border-radius:2px}
.note{left:171px;top:939px;font:400 13px "Raleway",sans-serif;color:#666}
.bar{left:170px;top:964px;width:860px;height:54px;background:var(--ink);display:flex;align-items:center;padding-left:13px;font:500 19px "Raleway",sans-serif;color:#8a8a8a}
.socials{display:flex;gap:5px;margin-left:14px}
.socials i{width:24px;height:24px;border:2px solid var(--teal);border-radius:50%}
.bar .sep{height:30px;border-left:1px dashed #555;margin:0 20px 0 25px}
.bar .phone{color:var(--white);font:600 24px "Raleway",sans-serif;margin-left:14px}
.copy{left:170px;top:1051px;font:400 10px/12px "Raleway",sans-serif;color:#888}
</style>
</head>
<body>
<div class="abs sky"></div>
<div class="abs topbar"></div>
<div class="abs stripe"></div>

<div class="abs lang">Select Your Langauge: <span class="flag"></span><span class="caret"></span></div>

<div class="abs logo"><span class="logo-name">Kelvar grupa</span><span class="logo-mark"></span></div>

<nav class="abs nav">
  <a href="#">HOME</a><a href="#">VIRTUAL PRIVATE SERVER</a><a href="#">ZENTOR APPS</a><a href="#">HOSTING</a><a href="#">CONTACT</a>
</nav>

<div class="abs hero" role="img" aria-label="Photo of a server room with a person on a laptop and a hand holding a glowing globe"></div>
<div class="abs hero-text">
  <div class="small">OUR SPECIALITY ARE IN AREA OF</div>
  <div class="big">INTERNET SERVICES</div>
  <div class="sub">AND INTERNET SERVERS TECHNOLOGY</div>
</div>

<div class="abs service" style="left:181px">
  <h3 style="left:68px">WEB</h3>
  <svg width="40" height="40" viewBox="0 0 40 40"><circle cx="20" cy="20" r="19" fill="#fff"/><circle cx="20" cy="20" r="14" fill="none" stroke="#1a1a1a" stroke-width="2"/><ellipse cx="20" cy="20" rx="6" ry="14" fill="none" stroke="#1a1a1a" stroke-width="2"/><line x1="6" y1="20" x2="34" y2="20" stroke="#1a1a1a" stroke-width="2"/></svg>
  <p style="left:68px">Lorem ipsum dolor sit amet, consectetuer adipiscing elit, sed diam nonummy ...</p>
  <span class="notch"></span>
</div>
<div class="abs service" style="left:392px">
  <h3 style="left:66px">DNS</h3>
  <svg width="40" height="40" viewBox="0 0 40 40"><circle cx="20" cy="20" r="19" fill="#fff"/><rect x="9" y="16" width="13" height="8" rx="4" fill="none" stroke="#1a1a1a" stroke-width="3" transform="rotate(-45 15 20)"/><rect x="18" y="16" width="13" height="8" rx="4" fill="none" stroke="#1a1a1a" stroke-width="3" transform="rotate(-45 25 20)"/></svg>
  <p style="left:66px">Lorem ipsum dolor sit amet, consectetuer adipiscing elit, sed diam nonummy ...</p>
  <span class="notch"></span>
</div>
<div class="abs service" style="left:603px">
  <h3 style="left:67px">BACKUPS</h3>
  <svg width="40" height="40" viewBox="0 0 40 40"><rect x="3" y="5" width="34" height="10" rx="2" fill="none" stroke="#fff" stroke-width="3"/><rect x="3" y="18" width="34" height="10" rx="2" fill="none" stroke="#fff" stroke-width="3"/><line x1="20" y1="28" x2="20" y2="35" stroke="#fff" stroke-width="3"/><line x1="8" y1="35" x2="32" y2="35" stroke="#fff" stroke-width="3"/></svg>
  <p style="left:67px">Lorem ipsum dolor sit amet, consectetuer adipiscing elit, sed diam nonummy ...</p>
  <span class="notch"></span>
</div>
<div class="abs service" style="left:813px">
  <h3 style="left:80px">EMAIL</h3>
  <svg width="44" height="40" viewBox="0 0 44 40"><rect x="2" y="6" width="40" height="28" fill="#fff"/><polyline points="4,8 22,24 40,8" fill="none" stroke="#1a1a1a" stroke-width="2.5"/><line x1="4" y1="32" x2="17" y2="19" stroke="#1a1a1a" stroke-width="2"/><line x1="40" y1="32" x2="27" y2="19" stroke="#1a1a1a" stroke-width="2"/></svg>
  <p style="left:80px">Lorem ipsum dolor sit amet, consectetuer adipiscing elit, sed diam nonummy ...</p>
</div>

<h1 class="abs welcome">Welcome</h1>
<div class="abs vdivider"></div>
<div class="abs intro">
  <h2>Halvorix and Tandix Certified Professionals</h2>
  <p>We are a company that configures and maintains web servers and builds advanced IT solutions to support their business. Our clients are companies that uses its advanced IT solutions in the form of dedicated servers, virtual servers (VPS), private networks (VPN) and online backup on Fenestra and Tandix platforms. <a href="#">Read More</a></p>
</div>

<div class="abs hrule" style="top:759px"></div>

<svg class="abs news-icon" width="28" height="22" viewBox="0 0 28 22"><rect x="1" y="1" width="26" height="20" fill="none" stroke="#777" stroke-width="2"/><rect x="5" y="6" width="8" height="7" fill="#777"/><line x1="15" y1="7" x2="23" y2="7" stroke="#777" stroke-width="2"/><line x1="15" y1="12" x2="23" y2="12" stroke="#777" stroke-width="2"/><line x1="5" y1="17" x2="23" y2="17" stroke="#777" stroke-width="2"/></svg>
<h2 class="abs section-title" style="left:221px;top:783px">Lastest News</h2>

<div class="abs news-item" style="left:181px">
  <div class="date">11<span>JULY</span></div>
  <h4>Lorem ipsum dolor sit amet,</h4>
  <p>consectetur &nbsp;adipiscing elit. Maecenas.....</p>
  <span class="btn">Read More</span>
</div>
<div class="abs news-item" style="left:479px">
  <div class="date">11<span>JULY</span></div>
  <h4>Lorem ipsum dolor sit amet,</h4>
  <p>consectetur &nbsp;adipiscing elit. Maecenas.....</p>
  <span class="btn">Read More</span>
</div>

<div class="abs tw-divider"></div>
<h2 class="abs section-title" style="left:801px;top:783px">Plonkit Tweets</h2>
<div class="abs tweet-dot"></div>
<div class="abs tweet">“The Great White Stallion” by @marenvoltdesigns.</div>
<div class="abs follow">@ Follow Us</div>

<div class="abs hrule" style="top:926px"></div>
<p class="abs note">We also provide service and sales of Zentor Apps and Halvorix Quorvo365 for which we are certified by Zentor and Halvorix.</p>

<div class="abs bar">
  We are Social. Follow Us.
  <span class="socials"><i></i><i></i><i></i><i></i></span>
  <span class="sep"></span>
  Need Help. Call Us Today.
  <span class="phone">+385 91 4470 318</span>
</div>

<div class="abs hrule" style="top:1037px"></div>
<p class="abs copy">Copyrights © KelvarGrupa. Privacy Policy &nbsp;| &nbsp;Terms &amp; Conditions<br>All rights reserved.</p>
</body>
</html>
```